Website for IT consulting Company

I need a website upgrade, the existing site content is ok, I would also like to add a testimonial page, the site should be something that is easy for us to update content. You use the content from www.kavnex.com as an example. I will also post update logo and artwork. I also need a contact form with some type of validation or captcha.

I added Coded to the Project

Please omit Address maps

Target Market(s)

small business, service oriented companies. We provide IT Consulting, support and mangement

Industry/Entity Type

Information Technology

Coding

Coded - Design and coding required

Number of Pages Required

1 page

Font styles to use
Serif
Sans Serif

Requirements
Must have
• Contain logo attached, and content from existing web site www.kavnex.com.
• Also need to update content easily, and be movable to different platforms.
• There is a catch phrase
• "Let us worry about your technology…” “ so you don’t have to!”
• Should be included.
Nice to have
• Testimonial page, Project page where we can post new and past projects and pictures
Should not have
• none

```html
<!DOCTYPE html>
<html lang="en">
<head>
<meta charset="utf-8">
<title>Kavnex — IT Solutions</title>
<link href="https://fonts.googleapis.com/css2?family=Roboto:wght@100;300;400;500;700&display=swap" rel="stylesheet">
<style>
:root{
  --orange:#f29a2e;
  --orange-dark:#e8872a;
  --ink:#333333;
  --text:#555555;
  --black:#000000;
  --bar:#eeeeee;
  --white:#ffffff;
}
*{box-sizing:border-box;margin:0;padding:0}
html,body{width:1200px;height:1131px;overflow:hidden;background:var(--white);font-family:"Roboto",sans-serif;color:var(--ink)}
.site-header{position:relative;height:118px;background:var(--bar);border-bottom:1px solid #dddddd}
.brand{position:absolute;left:0;top:0;width:351px;height:118px;background:var(--black);display:flex;align-items:center;padding-left:88px;gap:10px}
.brand-mark{width:24px;height:24px;background:var(--orange)}
.brand-name{color:var(--white);font-weight:500;font-size:34px;letter-spacing:1px;line-height:1}
.topbar{position:absolute;left:351px;right:0;top:0;height:45px;border-bottom:1px solid #d8d8d8;display:flex;align-items:center;padding-left:23px;font-size:15px;color:#222}
.topbar .item{display:flex;align-items:center;gap:7px;margin-right:10px}
.topbar svg{fill:var(--orange)}
.social{position:absolute;right:86px;top:9px;display:flex;gap:4px}
.social span{width:24px;height:24px;border:1px solid #bbbbbb;border-radius:50%;display:block}
.main-nav{position:absolute;left:383px;top:45px;height:73px;display:flex;align-items:center}
.main-nav a{font-size:13.5px;color:#222;text-decoration:none;padding:0 16px;height:73px;display:flex;align-items:center;position:relative}
.main-nav a.active{color:var(--orange)}
.main-nav a.active::before{content:"";position:absolute;left:0;right:0;top:0;height:3px;background:var(--orange)}
.hero{position:relative;height:497px;overflow:hidden}
.hero-photo{position:absolute;inset:0;background:
 radial-gradient(ellipse at 60% 55%,#6b4b30 0%,#3b2a1e 35%,transparent 65%),
 radial-gradient(ellipse at 92% 70%,#7a2a1a 0%,transparent 45%),
 linear-gradient(90deg,#0d0b0a 0%,#1e1813 35%,#2d2119 70%,#3a1e14 100%)}
.hero-copy{position:absolute;left:86px;top:172px;color:var(--white)}
.hero-title{font-weight:100;font-size:65px;line-height:1;letter-spacing:1px}
.hero-sub{font-weight:400;font-size:19px;margin-top:1px;padding-bottom:8px;border-bottom:1px solid #777;width:407px}
.hero-lead{font-size:14.5px;font-weight:400;margin-top:15px}
.btn{display:inline-block;margin-top:14px;background:var(--orange);color:#222;font-size:12px;padding:9px 24px;text-decoration:none}
.dots{position:absolute;right:86px;top:455px;display:flex;gap:2px}
.dots span{width:13px;height:13px;border:1.5px solid var(--white);border-radius:50%}
.dots span.on{border-color:var(--orange)}
.services{position:relative;height:516px}
.section-title{position:absolute;top:60px;left:0;right:0;display:flex;justify-content:center;align-items:center}
.section-title .rule{width:188px;height:1px;background:#999}
.section-title .tick{width:3px;height:30px;background:var(--orange)}
.section-title h2{font-weight:300;font-size:43px;color:#222;padding:0 16px;letter-spacing:.5px}
.cards{position:absolute;top:171px;left:86px;display:flex;gap:26px}
.card{position:relative;width:325px;height:272px;border:1px solid #cccccc;text-align:center}
.card-icon{position:absolute;top:-14px;left:121px;width:82px;height:82px;background:linear-gradient(135deg,var(--orange) 50%,var(--orange-dark) 50%);display:flex;align-items:center;justify-content:center}
.card h3{position:absolute;top:111px;left:10px;right:10px;color:var(--orange);font-weight:700;font-size:15.5px;line-height:1;text-transform:uppercase}
.card h3::after{content:"";display:block;width:48px;height:2px;background:#444;margin:8px auto 0}
.card p{position:absolute;top:154px;left:14px;right:14px;font-size:13.8px;line-height:1.34;color:var(--text);font-weight:400}
.more{position:absolute;top:243px;left:0;right:0;color:var(--orange);font-size:11px;font-weight:700}
</style>
</head>
<body>
<header class="site-header">
  <div class="brand">
    <span class="brand-mark"></span>
    <span class="brand-name">KAVNEX</span>
  </div>
  <div class="topbar">
    <span class="item"><svg width="12" height="12" viewBox="0 0 24 24"><path d="M6.6 10.8a15.1 15.1 0 0 0 6.6 6.6l2.2-2.2a1 1 0 0 1 1-.25 11.4 11.4 0 0 0 3.6.6 1 1 0 0 1 1 1V20a1 1 0 0 1-1 1A17 17 0 0 1 3 4a1 1 0 0 1 1-1h3.5a1 1 0 0 1 1 1c0 1.25.2 2.45.6 3.6a1 1 0 0 1-.25 1z"/></svg>(555) 214 - 7730</span>
    <span class="item"><svg width="15" height="11" viewBox="0 0 24 18"><path d="M0 0h24v2l-12 8L0 2z"/><path d="M0 4.5l12 8 12-8V18H0z"/></svg>info@kavnex.com</span>
    <div class="social"><span></span><span></span><span></span><span></span></div>
  </div>
  <nav class="main-nav">
    <a class="active">HOME</a><a>ABOUT US</a><a>SUPPORT</a><a>SERVICES</a><a>TESTIMONIALS</a><a>CLIENTS</a><a>CAREERS</a><a>CONTACT US</a>
  </nav>
</header>

<section class="hero">
  <div class="hero-photo" role="img" aria-label="Team working around a wooden table with laptops, notebooks and drinks"></div>
  <div class="hero-copy">
    <h1 class="hero-title">IT SOLUTIONS</h1>
    <p class="hero-sub">THAT WORK FOR YOUR BUSINESS.</p>
    <p class="hero-lead">A Full Service Technology Company.</p>
    <a class="btn">READ MORE</a>
  </div>
  <div class="dots"><span></span><span class="on"></span><span></span></div>
</section>

<section class="services">
  <div class="section-title"><span class="rule"></span><span class="tick"></span><h2>OUR SERVICES</h2><span class="tick"></span><span class="rule"></span></div>
  <div class="cards">
    <article class="card">
      <div class="card-icon"><svg width="58" height="50" viewBox="0 0 58 50" fill="none" stroke="#fff" stroke-width="1.8"><circle cx="20" cy="20" r="10"/><circle cx="20" cy="20" r="4"/><circle cx="40" cy="34" r="8"/><circle cx="40" cy="34" r="3"/><path d="M20 6v4M20 30v4M6 20h4M30 20h4M10 10l3 3M27 27l3 3M10 30l3-3M27 13l3-3M40 22v4M40 42v4M28 34h4M48 34h4"/></svg></div>
      <h3>Managed IT Solutions</h3>
      <p>Our staff will design, service, administer and maintain your IT needs. We are well versed on all major operating system, and network appliances</p>
      <span class="more">[ MORE... ]</span>
    </article>
    <article class="card">
      <div class="card-icon"><svg width="54" height="40" viewBox="0 0 54 40" fill="none" stroke="#fff" stroke-width="2"><rect x="9" y="4" width="36" height="25"/><path d="M3 33h48l-3 4H6z"/><path d="M25 13l0 9 2-2 2 4" stroke-width="1.5"/></svg></div>
      <h3>Remote Diagnostic and Support</h3>
      <p>Do you need a quick solution to a technical problem? With our live remote-assistance tool, a member of our support team can view your desktop</p>
      <span class="more">[ MORE... ]</span>
    </article>
    <article class="card">
      <div class="card-icon"><svg width="50" height="50" viewBox="0 0 50 50" fill="none" stroke="#fff" stroke-width="2"><rect x="8" y="5" width="24" height="40" rx="12"/><path d="M8 22h24M20 5v17"/><path d="M38 14v24c0 4 4 4 4 0V18"/></svg></div>
      <h3>IT Infrastructure Design<br>and Installation</h3>
      <p>Do you have more than one site? Do you need remote access? We can design and implement LANS/WANS and VPN's. Make your important data available</p>
      <span class="more">[ MORE... ]</span>
    </article>
  </div>
</section>
</body>
</html>
```